The Breezeway Baron
Air Conditioning & Heating
Attention Designers,
.AI format logo file has been uploaded with this project.
Thanks
Like #56 but need TACLB81947K license# on cards
Im sorry Torvellograph, when I started this project it was to get a new logo, and then pay the additional to add business cards etc. I am trying to get away from the castle and the clouds logo. Thanks

```html
<!DOCTYPE html>
<html lang="en">
<head>
<meta charset="utf-8">
<title>The Breezeway Baron – Stationery</title>
<link href="https://fonts.googleapis.com/css2?family=Roboto:wght@400;700;900&display=swap" rel="stylesheet">
<style>
:root{
  --bg:#2e2e2e;
  --paper:#ffffff;
  --navy:#1a3f8f;
  --blue:#2557b8;
  --orange:#f28a12;
  --red:#d9261c;
  --ink:#555;
  --edge:#d8d8d8;
}
*{margin:0;padding:0;box-sizing:border-box}
html,body{width:1200px;height:346px;overflow:hidden;background:var(--bg);font-family:"Roboto",Arial,sans-serif}
.canvas{position:relative;width:1200px;height:346px}
.piece{position:absolute;background:var(--paper);overflow:hidden;box-shadow:0 1px 3px rgba(0,0,0,.5)}
.brand{display:flex;align-items:center;gap:4px}
.brand-dot{border-radius:50%;background:var(--orange);flex:none}
.brand-name{font-weight:900;color:var(--navy);line-height:1;white-space:nowrap}
.tagline{color:var(--red);font-weight:700;line-height:1;white-space:nowrap}
.tiny{font-size:3.4px;color:var(--ink);line-height:1.35;white-space:nowrap}

/* flat artwork areas standing in for the brand wave */
.art-band{position:absolute;left:0;bottom:0;width:100%;background:linear-gradient(180deg,var(--orange) 0%,var(--blue) 45%,var(--navy) 100%)}
.art-flap{position:absolute;left:0;top:0;width:100%;height:38%}
.art-flap.warm{background:linear-gradient(180deg,var(--red),var(--orange))}
.art-flap.cool{background:linear-gradient(180deg,var(--navy),#5b8fe0)}
.art-flap.plain{background:#f4f4f4;border-bottom:1px solid var(--edge)}

.hero-logo{position:absolute;left:6px;top:6px}
.hero-logo .brand-dot{width:16px;height:16px}
.hero-logo .brand-name{font-size:15px;color:#fff}
.hero-logo .tagline{font-size:7px;margin:3px 0 0 20px;color:var(--orange)}
.set-label{position:absolute;left:30px;top:110px;font-size:6px;color:#ccc}

.card{width:125px;height:60px;left:19px}
.card .brand{position:absolute;left:6px;top:8px}
.card .brand-dot{width:8px;height:8px}
.card .brand-name{font-size:8px}
.card .tagline{position:absolute;left:18px;top:19px;font-size:4px}
.card .tiny{position:absolute;left:80px;top:24px}
.card .art-band{height:14px}

.letterhead{width:226px;height:312px;top:19px}
.letterhead .brand{position:absolute;left:10px;top:18px}
.letterhead .brand-dot{width:10px;height:10px}
.letterhead .brand-name{font-size:10px}
.letterhead .tagline{position:absolute;left:24px;top:31px;font-size:4.5px}
.letterhead .contact{position:absolute;left:170px;top:12px}
.letterhead .art-band{height:30px}
.letterhead .web{position:absolute;bottom:6px;left:0;width:100%;text-align:center;color:#fff;font-size:4px}

.envelope{width:250px;height:91px;left:643px}
.envelope .brand{position:absolute;left:8px;top:8px}
.envelope .brand-dot{width:8px;height:8px}
.envelope .brand-name{font-size:8px}
.envelope .tagline{position:absolute;left:20px;top:19px;font-size:3.8px}
.envelope .contact{position:absolute;left:20px;top:25px}
.envelope .art-band{height:16px}
.envelope .web{position:absolute;bottom:4px;left:0;width:100%;text-align:center;color:#fff;font-size:3.6px}

.env-back{width:283px;height:96px;left:907px}
</style>
</head>
<body>
<main class="canvas">

  <div class="hero-logo">
    <div class="brand"><span class="brand-dot"></span><span class="brand-name">The Breezeway Baron</span></div>
    <div class="tagline">Air Conditioning &amp; Heating</div>
  </div>
  <div class="set-label">Stationery Concepts</div>

  <section class="piece card" style="top:132px">
    <div class="brand"><span class="brand-dot"></span><span class="brand-name">The Breezeway Baron</span></div>
    <div class="tagline">Air Conditioning &amp; Heating</div>
    <div class="tiny">Ph: 813-555-0147<br>TACLB81947K</div>
    <div class="art-band" role="img" aria-label="Brand wave artwork in blue and orange"></div>
  </section>

  <section class="piece card" style="top:235px">
    <div class="brand"><span class="brand-dot"></span><span class="brand-name">The Breezeway Baron</span></div>
    <div class="tagline">Air Conditioning &amp; Heating</div>
    <div class="art-band" role="img" aria-label="Brand wave artwork in blue and orange"></div>
  </section>

  <section class="piece letterhead" style="left:163px">
    <div class="brand"><span class="brand-dot"></span><span class="brand-name">The Breezeway Baron</span></div>
    <div class="tagline">Air Conditioning &amp; Heating</div>
    <div class="tiny contact">1840 Harbor Lane<br>Tampa, FL 33602<br>Ph: 813-555-0147<br>License TACLB81947K</div>
    <div class="art-band" role="img" aria-label="Brand wave artwork in blue, red and orange"></div>
    <div class="web">www.thebreezewaybaronhv.com</div>
  </section>

  <section class="piece letterhead" style="left:403px">
    <div class="brand"><span class="brand-dot"></span><span class="brand-name">The Breezeway Baron</span></div>
    <div class="tagline">Air Conditioning &amp; Heating</div>
    <div class="tiny contact">1840 Harbor Lane<br>Tampa, FL 33602<br>Ph: 813-555-0147<br>License TACLB81947K</div>
    <div class="art-band" role="img" aria-label="Brand wave artwork in blue, red and orange"></div>
    <div class="web">www.thebreezewaybaronhv.com</div>
  </section>

  <section class="piece envelope" style="top:125px">
    <div class="brand"><span class="brand-dot"></span><span class="brand-name">The Breezeway Baron</span></div>
    <div class="tagline">Air Conditioning &amp; Heating</div>
    <div class="tiny contact">1840 Harbor Lane<br>Tampa, FL 33602</div>
    <div class="art-band" role="img" aria-label="Brand wave artwork in blue and orange"></div>
    <div class="web">www.thebreezewaybaronhv.com</div>
  </section>

  <section class="piece envelope" style="top:223px">
    <div class="brand"><span class="brand-dot"></span><span class="brand-name">The Breezeway Baron</span></div>
    <div class="tagline">Air Conditioning &amp; Heating</div>
    <div class="tiny contact">1840 Harbor Lane<br>Tampa, FL 33602</div>
    <div class="art-band" role="img" aria-label="Brand wave artwork in blue and orange"></div>
    <div class="web">www.thebreezewaybaronhv.com</div>
  </section>

  <section class="piece env-back" style="top:48px">
    <div class="art-flap warm" role="img" aria-label="Envelope flap artwork in warm red and orange"></div>
  </section>

  <section class="piece env-back" style="top:132px">
    <div class="art-flap cool" role="img" aria-label="Envelope flap artwork in cool blue"></div>
  </section>

  <section class="piece env-back" style="top:228px">
    <div class="art-flap plain"></div>
  </section>

</main>
</body>
</html>
```